Web page for Marcus Penrose Chartered Tax Adviser

I need to take the basic web page that I have created and "Brand it" to be compatible with the corporate logo and stationery created for me by other Pixel Guild designers.
I will need a watermark as well as a distinctive home page and then a branded general page for content including a series of Blogs.

Target Market(s)

My practice deals with expatriates including those looking to invest in Australia.

Industry/Entity Type

Crowd

Font styles to use
Other font styles liked:
• Per logo

Requirements
Must have
• Besides the homepage I will need a general page for content, branded in the same style as the letterheads.
Nice to have
• A watermark to go with the blogs and news content.

```html
<!DOCTYPE html>
<html lang="en">
<head>
<meta charset="utf-8">
<title>Marcus Penrose Chartered Tax Adviser</title>
<link href="https://fonts.googleapis.com/css2?family=Open+Sans:wght@400;600;700&family=Roboto+Slab:wght@300;400;700&display=swap" rel="stylesheet">
<style>
:root{
  --navy:#1f3d63;
  --blue:#336091;
  --blue-light:#4d80b5;
  --ink:#2a2f36;
  --muted:#7b828b;
  --paper:#ffffff;
  --mist:#f1f2f4;
  --night:#1b1f25;
  --slab:"Roboto Slab", Georgia, serif;
  --sans:"Open Sans", Arial, sans-serif;
}
*{box-sizing:border-box;margin:0;padding:0}
html,body{width:1200px;height:2632px;overflow:hidden}
body{font-family:var(--sans);color:var(--ink);background:var(--paper)}

/* Hero */
.hero{position:relative;height:540px;text-align:center;color:#fff}
.hero-photo{position:absolute;inset:0;background:linear-gradient(180deg,#3a3f47 0%,#23272d 55%,#2e333a 100%)}
.hero-inner{position:relative;padding-top:86px}
.brand-mark{display:inline-flex;align-items:center;gap:18px;font-family:var(--slab);font-weight:700;letter-spacing:2px}
.hero .brand-mark{flex-direction:column;font-size:26px;color:#fff}
.circle{border-radius:50%;display:inline-block}
.hero .circle{width:92px;height:92px;border:4px solid #fff}
.hero-title{margin-top:40px;font-family:var(--slab);font-weight:700;font-size:34px;letter-spacing:2px}
.hero-sub{width:460px;margin:14px auto 0;font-size:13px;line-height:19px;color:#d6d9de}
.btn{display:inline-block;font-family:var(--sans);font-weight:700;font-size:11px;letter-spacing:1px;text-transform:uppercase}
.btn-light{margin-top:30px;background:#fff;color:var(--navy);width:136px;height:44px;line-height:44px}

/* Navigation */
.site-nav{height:100px;display:flex;align-items:center;justify-content:space-between;padding:0 190px 0 172px;border-bottom:1px solid #e3e5e8}
.site-nav .brand-mark{color:var(--navy);gap:14px}
.site-nav .circle{width:44px;height:44px;background:var(--navy)}
.brand-text{display:flex;flex-direction:column;text-align:left}
.brand-name{font-size:24px;line-height:26px}
.brand-role{font-family:var(--sans);font-size:9px;letter-spacing:2px;font-weight:600;color:var(--muted)}
.nav-links{display:flex;align-self:stretch;padding-top:4px}
.nav-links a{width:92px;display:flex;align-items:center;justify-content:center;font-size:10px;font-weight:700;letter-spacing:1px;color:var(--navy);text-decoration:none}
.nav-links a.active{background:var(--navy);color:#fff}

/* Tagline */
.tagline{height:420px;background:var(--mist);text-align:center;padding-top:66px}
.tagline h1{font-family:var(--slab);font-weight:300;font-size:66px;line-height:74px;color:#5c7fa3;letter-spacing:2px}
.tagline strong{font-weight:700;color:var(--navy)}
.tagline .circle{margin-top:30px;width:40px;height:40px;border:3px solid #a9b7c6}

/* Welcome band */
.welcome{margin-top:8px;height:132px;background:var(--blue);display:flex;align-items:center;color:#fff}
.welcome-title{width:420px;padding-left:172px;background:var(--navy);height:100%;display:flex;flex-direction:column;justify-content:center;font-family:var(--slab)}
.welcome-title h2{font-size:36px;font-weight:700;letter-spacing:1px}
.welcome-title span{font-size:15px;letter-spacing:3px;color:#c8d6e6}
.welcome p{width:380px;margin-left:40px;font-size:11px;line-height:17px;color:#dbe5f0}
.btn-blue{margin-left:34px;background:var(--blue-light);color:#fff;width:160px;height:42px;line-height:42px;text-align:center}

/* Services */
.services{padding-top:40px;text-align:center;height:632px}
.section-title{font-family:var(--slab);font-weight:700;font-size:44px;color:var(--navy);letter-spacing:1px}
.section-sub{margin-top:6px;font-size:12px;letter-spacing:2px;color:var(--muted);font-weight:600}
.service-row{display:flex;justify-content:center;gap:76px;margin-top:30px}
.service{width:220px}
.hex{width:220px;height:240px;margin:0 auto;clip-path:polygon(50% 0,100% 25%,100% 75%,50% 100%,0 75%,0 25%);background:var(--navy);display:flex;align-items:center;justify-content:center}
.hex-photo{width:206px;height:226px;clip-path:polygon(50% 0,100% 25%,100% 75%,50% 100%,0 75%,0 25%)}
.photo-invest{background:linear-gradient(160deg,#c9d6e3,#7f95ad)}
.photo-wealth{background:linear-gradient(160deg,#d8dde3,#4a5a6e)}
.photo-tax{background:linear-gradient(160deg,#e6e3df,#a59c92)}
.service h3{margin-top:22px;font-family:var(--slab);font-weight:700;font-size:24px;line-height:26px;color:var(--navy)}
.service h3 span{display:block;font-weight:300;color:#5c7fa3}
.service p{margin-top:12px;font-size:11px;line-height:17px;color:var(--muted)}
.btn-navy{margin-top:18px;background:var(--navy);color:#fff;width:96px;height:30px;line-height:30px;font-size:9px}

/* Reviews */
.reviews{position:relative;height:312px;color:#fff}
.reviews-photo{position:absolute;inset:0;background:linear-gradient(120deg,#2d5786,#3d6c9e 60%,#2f5a89)}
.reviews-inner{position:relative;text-align:center;padding-top:28px}
.reviews .section-title{color:#fff;font-size:38px}
.reviews .section-sub{color:#c8d6e6}
.review{display:flex;align-items:flex-start;margin:26px 0 0 206px;text-align:left}
.reviewer{width:116px;text-align:center}
.reviewer .hex{width:110px;height:120px;background:#fff}
.reviewer .hex-photo{width:102px;height:112px;background:linear-gradient(160deg,#e3d6cc,#9c8678)}
.reviewer span{display:block;margin-top:8px;font-size:10px;font-weight:700;letter-spacing:1px}
.quote{position:relative;width:600px;margin-left:40px;padding:18px 30px;font-size:12px;line-height:19px;color:#e3ebf4}
.quote::before,.quote::after{position:absolute;font-family:var(--slab);font-size:60px;color:#8fb0d3}
.quote::before{content:"\201C";left:0;top:-4px}
.quote::after{content:"\201D";right:-60px;bottom:-44px}
.dots{position:absolute;left:0;right:0;bottom:18px;display:flex;justify-content:center;gap:8px}
.dots i{width:8px;height:8px;border-radius:50%;border:1px solid #fff}
.dots i:first-child{background:#fff}

/* Contact strip */
.contact-strip{height:148px;display:flex;align-items:center;justify-content:center}
.contact-item{width:290px;display:flex;align-items:center;gap:16px;padding-left:36px;color:var(--navy)}
.contact-item + .contact-item{border-left:1px solid #d8dce1}
.contact-item .circle{width:38px;height:38px;background:var(--navy)}
.contact-item svg{width:38px;height:38px}
.contact-item strong{display:block;font-family:var(--slab);font-size:20px}
.contact-item small{font-size:10px;color:var(--muted);letter-spacing:1px}

/* Footer */
.site-footer{position:relative;height:304px;text-align:center;color:#fff}
.footer-photo{position:absolute;inset:0;background:linear-gradient(180deg,#2e333a,#16191e)}
.footer-inner{position:relative;padding-top:36px}
.site-footer .brand-mark{flex-direction:column;gap:10px;font-size:18px}
.site-footer .circle{width:60px;height:60px;border:3px solid #fff}
.footer-note{margin-top:10px;font-size:10px;letter-spacing:1px;color:#aab1ba}
.social{display:flex;justify-content:center;gap:10px;margin-top:16px}
.social i{width:28px;height:28px;border-radius:50%;background:#3d434b;border:1px solid #5b626b}
.to-top{margin:24px auto 0;width:34px;height:34px;border-radius:50%;background:#3d434b;display:flex;align-items:center;justify-content:center}
</style>
</head>
<body>

<header class="hero">
  <div class="hero-photo" role="img" aria-label="Dark photograph of business people working over documents at a desk"></div>
  <div class="hero-inner">
    <div class="brand-mark"><span class="circle"></span>MARCUS PENROSE</div>
    <h2 class="hero-title">WE WILL SHOW YOU THE WAY TO SUCCESS !</h2>
    <p class="hero-sub">Clear, practical tax advice for expatriates and investors moving money, families and careers across borders.</p>
    <a class="btn btn-light">Read more now</a>
  </div>
</header>

<nav class="site-nav">
  <div class="brand-mark">
    <span class="circle"></span>
    <span class="brand-text"><span class="brand-name">MARCUS PENROSE</span><span class="brand-role">CHARTERED TAX ADVISER</span></span>
  </div>
  <div class="nav-links">
    <a class="active">HOME</a><a>ABOUT</a><a>BLOG</a><a>NEWS</a><a>CONTACT</a>
  </div>
</nav>

<section class="tagline">
  <h1>BEAUTIFUL <strong>WORK</strong><br>BY <strong>PASSIONATE</strong><br>PEOPLE.</h1>
  <span class="circle"></span>
</section>

<section class="welcome">
  <div class="welcome-title"><h2>WELCOME !</h2><span>MARCUS PENROSE</span></div>
  <p>Expatriates and overseas investors rely on us for careful planning, honest answers and returns filed on time, so that every move into Australia is made with full confidence.</p>
  <a class="btn btn-blue">Read more</a>
</section>

<section class="services">
  <h2 class="section-title">CHARTERED TAX ADVISER</h2>
  <p class="section-sub">PLANNING, INVESTMENT AND COMPLIANCE FOR EXPATRIATES</p>
  <div class="service-row">
    <article class="service">
      <div class="hex"><div class="hex-photo photo-invest" role="img" aria-label="Photograph of a team reviewing investment charts"></div></div>
      <h3>INVESTMENT<span>MANAGEMENT</span></h3>
      <p>Structured advice on property, shares and funds so your Australian investments stay efficient and fully compliant.</p>
      <a class="btn btn-navy">Read more</a>
    </article>
    <article class="service">
      <div class="hex"><div class="hex-photo photo-wealth" role="img" aria-label="Photograph of a business adviser in a suit"></div></div>
      <h3>WEALTH<span>MANAGEMENT</span></h3>
      <p>Long-term plans that protect what you have built, from pensions and trusts to family wealth transfers.</p>
      <a class="btn btn-navy">Read more</a>
    </article>
    <article class="service">
      <div class="hex"><div class="hex-photo photo-tax" role="img" aria-label="Photograph of colleagues meeting in a bright office"></div></div>
      <h3>TAX<span>ADVISORY</span></h3>
      <p>Returns, residency reviews and double tax relief handled precisely, leaving you free to focus on life abroad.</p>
      <a class="btn btn-navy">Read more</a>
    </article>
  </div>
</section>

<section class="reviews">
  <div class="reviews-photo" role="img" aria-label="Blue tinted photograph of an office meeting"></div>
  <div class="reviews-inner">
    <h2 class="section-title">HAPPY CLIENTS REVIEWS</h2>
    <p class="section-sub">WHAT OUR EXPATRIATE CLIENTS SAY ABOUT US</p>
    <div class="review">
      <div class="reviewer">
        <div class="hex"><div class="hex-photo" role="img" aria-label="Portrait photograph of a smiling client"></div></div>
        <span>MRS CLARA</span>
      </div>
      <blockquote class="quote">Moving to Perth felt overwhelming until Marcus took over our taxes. Every question was answered quickly and we finally understand where our money goes.</blockquote>
    </div>
  </div>
  <div class="dots"><i></i><i></i><i></i></div>
</section>

<section class="contact-strip">
  <div class="contact-item">
    <span class="circle"></span>
    <div><strong>MARCUS PENROSE</strong><small>14 Harbour Lane, Brisbane QLD</small></div>
  </div>
  <div class="contact-item">
    <svg viewBox="0 0 24 24" aria-hidden="true"><path fill="#1f3d63" d="M6.6 10.8a15.2 15.2 0 0 0 6.6 6.6l2.2-2.2c.3-.3.7-.4 1-.2 1.1.4 2.3.6 3.6.6.6 0 1 .4 1 1V20c0 .6-.4 1-1 1A17 17 0 0 1 3 4c0-.6.4-1 1-1h3.5c.6 0 1 .4 1 1 0 1.3.2 2.5.6 3.6.1.3 0 .7-.2 1z"/></svg>
    <div><strong>CALL US NOW</strong><small>(07) 5550 1234</small></div>
  </div>
  <div class="contact-item">
    <svg viewBox="0 0 24 24" aria-hidden="true"><rect x="2" y="5" width="20" height="14" rx="1" fill="none" stroke="#1f3d63" stroke-width="2"/><path d="M2 6l10 7 10-7" fill="none" stroke="#1f3d63" stroke-width="2"/></svg>
    <div><strong>SEND US MAIL</strong><small>hello@penrosetax.example</small></div>
  </div>
</section>

<footer class="site-footer">
  <div class="footer-photo" role="img" aria-label="Dark photograph of a business desk with papers"></div>
  <div class="footer-inner">
    <div class="brand-mark"><span class="circle"></span>MARCUS PENROSE</div>
    <p class="footer-note">MARCUS PENROSE CHARTERED TAX ADVISER · All rights reserved</p>
    <div class="social"><i></i><i></i><i></i><i></i></div>
    <div class="to-top"><svg width="14" height="10" viewBox="0 0 14 10" aria-hidden="true"><path d="M1 9l6-7 6 7" fill="none" stroke="#fff" stroke-width="2"/></svg></div>
  </div>
</footer>

</body>
</html>
```